Simple elegant feminine design - Going out on my own as a Mortgage Broker.
My thoughts are the following details on the Front, middle of the card possibly? Phone and email smaller font than my name?
Marnie Veltrin
Finance Specialist
p: 0438 215 962
e: marnie@veltrinlending.com.au
Bottom of the card
residential / commercial / equipment
I would like the Font in Rose Gold maybe white or black background? or Possibly a stone grey - are you able to do a few options? I'd like them embossed
Then I had an idea as a simple logo as per the attached if you get the idea in my scribble, my initials, capital M attached to a small v that leads/follows into a circle? Thicker Font In Rose Gold, middle of the card at the back.
Very open to ideas though and what colour you think would look better with the Rose Gold.
Thanks so much for your help, I am not very creative and savvy with this stuff :-)
Industry/Entity Type
Finance
Contact Information for Business Card
Marnie Veltrin
p: 0438 215 962
Look and feel

```html
<!DOCTYPE html>
<html lang="en">
<head>
<meta charset="utf-8">
<title>Marnie Veltrin – Business Cards</title>
<link rel="stylesheet" href="https://fonts.googleapis.com/css2?family=Montserrat:wght@300;400;500&display=swap">
<style>
  :root {
    --backdrop: #2f3131;
    --card-stock: #ddd5cc;
    --rose-gold: #b39470;
    --rose-gold-soft: #c4a887;
  }
  * { margin: 0; padding: 0; box-sizing: border-box; }
  html, body {
    width: 1200px;
    height: 900px;
    overflow: hidden;
    background: var(--backdrop);
    font-family: "Montserrat", sans-serif;
  }
  .sheet {
    position: relative;
    width: 1200px;
    height: 900px;
  }
  .card {
    position: absolute;
    width: 560px;
    height: 320px;
    background: var(--card-stock);
    border-radius: 26px;
    display: flex;
    flex-direction: column;
    align-items: center;
    justify-content: center;
    color: var(--rose-gold);
    box-shadow: 0 6px 18px rgba(0,0,0,0.35);
  }
  .card--front { left: 110px; top: 90px; }
  .card--back  { left: 530px; top: 490px; }

  .brand-mark {
    display: flex;
    align-items: center;
    gap: 10px;
    margin-bottom: 26px;
  }
  .brand-mark__dot {
    width: 14px;
    height: 14px;
    border-radius: 50%;
    background: var(--rose-gold);
  }
  .brand-mark__name {
    font-size: 22px;
    font-weight: 400;
    letter-spacing: 0.12em;
    color: var(--rose-gold);
  }

  .holder-name {
    font-size: 30px;
    font-weight: 400;
    letter-spacing: 0.06em;
    text-transform: uppercase;
    line-height: 1;
  }
  .holder-title {
    font-size: 13px;
    font-weight: 400;
    letter-spacing: 0.42em;
    text-transform: uppercase;
    margin-top: 8px;
    margin-left: 0.42em;
  }

  .contact-list {
    display: flex;
    gap: 28px;
    margin-top: 30px;
    font-size: 12px;
    font-weight: 500;
    color: var(--rose-gold-soft);
  }
  .contact-list__item {
    display: flex;
    align-items: center;
    gap: 6px;
  }
  .contact-list__icon {
    width: 15px;
    height: 12px;
  }
</style>
</head>
<body>
<main class="sheet">

  <section class="card card--front" aria-label="Business card front">
    <div class="brand-mark">
      <span class="brand-mark__dot"></span>
      <span class="brand-mark__name">Veltrin</span>
    </div>
    <h1 class="holder-name">Marnie Veltrin</h1>
    <p class="holder-title">Finance Specialist</p>
  </section>

  <section class="card card--back" aria-label="Business card back">
    <div class="brand-mark">
      <span class="brand-mark__dot"></span>
      <span class="brand-mark__name">Veltrin</span>
    </div>
    <h2 class="holder-name">Marnie Veltrin</h2>
    <p class="holder-title">Finance Specialist</p>
    <ul class="contact-list">
      <li class="contact-list__item">
        <svg class="contact-list__icon" viewBox="0 0 15 12" aria-hidden="true">
          <path d="M2 4 Q7.5 0 13 4 L11.5 5.5 L9.5 4.5 L9.5 3.5 Q7.5 2.8 5.5 3.5 L5.5 4.5 L3.5 5.5 Z" fill="none" stroke="currentColor" stroke-width="1"/>
          <rect x="4" y="6" width="7" height="5" rx="1" fill="none" stroke="currentColor" stroke-width="1"/>
        </svg>
        <span>0438 215 962</span>
      </li>
      <li class="contact-list__item">
        <svg class="contact-list__icon" viewBox="0 0 15 12" aria-hidden="true">
          <rect x="1" y="1.5" width="13" height="9" fill="none" stroke="currentColor" stroke-width="1"/>
          <path d="M1 1.5 L7.5 7 L14 1.5" fill="none" stroke="currentColor" stroke-width="1"/>
        </svg>
        <span>marnie.veltrin@veltrinmail.com</span>
      </li>
    </ul>
  </section>

</main>
</body>
</html>
```